New banner graphics for Kelbro.com website

I've developed a software tool that helps businesses ensure they are working on their most valuable and important work.

I would like a banner graphic for my home page (www.kelbro.com) that can somehow capture the value of focus and intentional outcomes.

I had an initial thought of a starry sky that shifts focus to a few bright stars, but while that might sound ok, I think my idea is lame hence I'm coming to you guys.

My sites two primary colors are a soft purple and gray.
#919EC1(purple)
#9E9E9E (gray)

Target Market(s)

B2B for enterprises. Typical customers are CFOs, CIOs/Heads of IT

Industry/Entity Type

Business Software

Number of Pages Required

1 page

Font styles to use
Sans Serif

Colors
b8a6cd
cedeed

Requirements
Must have
• I use Divi as my Wordpress theme and the current main landing page can be seen at www.kelbro.com.
• My logo colors are:
• #919EC1(purple)
• #9E9E9E (gray)
Should not have
• Lots of distraction or visual "noise". I want to re-enforce the message that my software is focused on their business and not my products or website.

```html
<!DOCTYPE html>
<html lang="en">
<head>
<meta charset="utf-8">
<title>Is Your Business Strategy</title>
<link rel="stylesheet" href="https://fonts.googleapis.com/css2?family=Oswald:wght@400;500&family=Open+Sans:ital,wght@0,600;1,300&display=swap">
<style>
  :root {
    --brand-purple: #919ec1;
    --brand-gray: #9e9e9e;
    --soft-lilac: #b8a6cd;
    --soft-mist: #cedeed;
    --deep-purple: #5e6790;
    --band-shade: rgba(60, 64, 96, 0.30);
    --band-light: rgba(206, 222, 237, 0.35);
    --ink: #ffffff;
    --ink-soft: rgba(255, 255, 255, 0.94);
    --frame-soft: rgba(255, 255, 255, 0.6);
  }
  * { box-sizing: border-box; margin: 0; padding: 0; }
  html, body {
    width: 1200px;
    height: 675px;
    overflow: hidden;
    background: var(--brand-purple);
  }
  .banner {
    position: relative;
    width: 1200px;
    height: 675px;
    overflow: hidden;
  }
  .banner__backdrop {
    position: absolute;
    inset: 0;
    background:
      radial-gradient(ellipse at 18% 25%, var(--soft-mist) 0%, transparent 50%),
      radial-gradient(ellipse at 82% 60%, var(--soft-lilac) 0%, transparent 45%),
      linear-gradient(160deg, var(--brand-purple) 0%, var(--deep-purple) 50%, var(--brand-gray) 100%);
  }
  .banner__band {
    position: absolute;
    left: 0;
    width: 100%;
  }
  .banner__band--focus {
    top: 142px;
    height: 401px;
    background: var(--band-shade);
  }
  .banner__band--base {
    top: 543px;
    height: 68px;
    background: var(--band-light);
  }
  .headline {
    position: absolute;
    top: 173px;
    left: 350px;
    width: 456px;
    height: 62px;
    border: 2px solid var(--ink);
    display: flex;
    align-items: center;
    justify-content: center;
    font-family: "Oswald", sans-serif;
    font-weight: 500;
    font-size: 38px;
    color: var(--ink);
  }
  .choices {
    position: absolute;
    top: 295px;
    left: 0;
    width: 100%;
    list-style: none;
  }
  .choice {
    position: relative;
    height: 33px;
    margin-bottom: 24.5px;
  }
  .choice__good {
    position: absolute;
    right: 742px;
    top: 0;
    height: 33px;
    padding: 0 7px;
    border: 2px solid var(--ink);
    display: flex;
    align-items: center;
    font-family: "Oswald", sans-serif;
    font-weight: 500;
    font-size: 24px;
    color: var(--ink);
    white-space: nowrap;
  }
  .choice__or {
    position: absolute;
    left: 479px;
    top: 0;
    width: 44px;
    height: 33px;
    line-height: 33px;
    text-align: center;
    font-family: "Open Sans", sans-serif;
    font-weight: 600;
    font-size: 26px;
    color: var(--ink);
  }
  .choice__weak {
    position: absolute;
    left: 541px;
    top: 0;
    height: 33px;
    padding: 0 5px;
    border: 1px solid var(--frame-soft);
    display: flex;
    align-items: center;
    font-family: "Open Sans", sans-serif;
    font-style: italic;
    font-weight: 300;
    font-size: 27px;
    color: var(--ink-soft);
    white-space: nowrap;
  }
</style>
</head>
<body>
  <main class="banner">
    <div class="banner__backdrop" role="img" aria-label="Purple and gray tinted photo collage of a businessman walking with a briefcase over a brick wall, with calendar pages, clocks, a world map, coins and a handshake"></div>
    <div class="banner__band banner__band--focus"></div>
    <div class="banner__band banner__band--base"></div>

    <h1 class="headline">Is Your Business Strategy</h1>

    <ul class="choices">
      <li class="choice">
        <span class="choice__good">WRITTEN DOWN</span>
        <span class="choice__or">OR</span>
        <span class="choice__weak">LOOSE THOUGHTS – ON THE&nbsp; BEST OF DAYS</span>
      </li>
      <li class="choice">
        <span class="choice__good">DRIVING PROJECTS</span>
        <span class="choice__or">OR</span>
        <span class="choice__weak">JUST A SET OF SLIDES TACKED TO WALLS</span>
      </li>
      <li class="choice">
        <span class="choice__good">SHARED WITH THE TEAM</span>
        <span class="choice__or">OR</span>
        <span class="choice__weak">KEPT TOP SECRET JUST TO BE SAFE</span>
      </li>
      <li class="choice">
        <span class="choice__good">MEASURABLE</span>
        <span class="choice__or">OR</span>
        <span class="choice__weak">MORE ART THAN SCIENCE</span>
      </li>
    </ul>
  </main>
</body>
</html>
```